parts and kits

we need an updated flyer to email to our customers
we need to have what we sell at kivo
caliper pistons
seal kits
new brake cylinders
brake boosters
brake shoes
brake pads
brake hoses
cables -accelerator, clutch, hand brake etc
for both private, vintage and commercial vehicles

```html
<!DOCTYPE html>
<html lang="en">
<head>
<meta charset="utf-8">
<title>Kivo Auto Centre – Brakes, Hoses and Cables</title>
<link href="https://fonts.googleapis.com/css2?family=Montserrat:wght@600;700;800;900&family=Open+Sans:wght@400;600;700&display=swap" rel="stylesheet">
<style>
  :root{
    --yellow:#f6b90d;
    --ink:#1d1e21;
    --ink-2:#2b2d31;
    --panel:#eceef1;
    --white:#ffffff;
    --muted:#5a5d63;
  }
  *{box-sizing:border-box;margin:0;padding:0}
  html,body{width:695px;height:1200px;overflow:hidden;background:var(--white)}
  .flyer{position:relative;width:695px;height:1200px;background:var(--ink);font-family:"Open Sans",Arial,sans-serif;color:var(--ink)}
  .hero{position:absolute;left:0;top:0;width:695px;height:380px;overflow:hidden}
  .hero-photo{position:absolute;inset:0;background:linear-gradient(100deg,#5b5f66 0%,#8d9299 30%,#b9bcc0 55%,#6f737a 80%,#3e4146 100%)}
  .hero-bands{position:absolute;left:0;top:0}
  .brand{position:absolute;left:0;right:0;top:300px;display:flex;justify-content:center;align-items:center;gap:10px}
  .brand-mark{width:22px;height:22px;background:var(--yellow)}
  .brand-name{font-family:"Montserrat",sans-serif;font-weight:900;font-size:34px;letter-spacing:3px;color:var(--white)}
  .headline{position:absolute;top:385px;left:0;right:0;text-align:center;font-family:"Montserrat",sans-serif;font-weight:900;color:var(--white);text-transform:uppercase;line-height:1.12}
  .headline .l1{font-size:31px}
  .headline .l2{font-size:27px}
  .products{position:absolute;top:480px;left:0;width:695px;height:340px;background:var(--panel)}
  .products-tag{position:absolute;left:50%;top:-12px;transform:translateX(-50%);background:var(--yellow);padding:8px 48px;font-family:"Montserrat",sans-serif;font-weight:900;font-size:22px;color:var(--ink);clip-path:polygon(6% 0,94% 0,100% 50%,94% 100%,6% 100%,0 50%)}
  .product-grid{position:absolute;top:52px;left:38px;right:20px;display:grid;grid-template-columns:1fr 1fr 1fr;row-gap:22px;column-gap:10px;list-style:none}
  .product{display:flex;align-items:center;gap:14px;font-weight:600;font-size:17px;line-height:1.2;color:var(--ink);min-height:46px}
  .product-icon{flex:none;width:42px;height:42px;border-radius:50%;background:var(--ink);display:flex;align-items:center;justify-content:center}
  .vehicles{position:absolute;top:820px;left:0;width:695px;height:46px;background:var(--ink-2);color:var(--white);text-align:center;font-weight:600;font-size:17px;line-height:46px}
  .parts-strip{position:absolute;top:866px;left:0;width:695px;height:160px;background:linear-gradient(180deg,#ffffff,#e9eaec)}
  .parts-strip .part{position:absolute;top:22px;height:116px;border-radius:10px;background:linear-gradient(160deg,#7c8087,#2f3136)}
  .aim{position:absolute;top:1026px;left:0;width:695px;height:52px;background:var(--yellow);text-align:center;font-family:"Montserrat",sans-serif;font-weight:800;font-size:16px;line-height:52px;text-transform:uppercase;color:var(--ink)}
  .contact{position:absolute;top:1078px;left:0;width:695px;height:122px;background:var(--ink);display:flex;justify-content:space-between;align-items:center;padding:0 26px;color:var(--white);font-size:14px}
  .contact-item{display:flex;align-items:center;gap:8px}
  .contact-icon{width:26px;height:26px;border-radius:50%;background:var(--yellow);display:flex;align-items:center;justify-content:center}
</style>
</head>
<body>
<main class="flyer">
  <header class="hero">
    <div class="hero-photo" role="img" aria-label="Photo collage of hands reconditioning brake calipers and a brake master cylinder"></div>
    <svg class="hero-bands" width="695" height="380" viewBox="0 0 695 380">
      <polygon points="0,190 0,235 300,380 395,380 695,235 695,190 347,360" fill="#f6b90d"/>
      <polygon points="0,235 0,380 300,380" fill="#1d1e21"/>
      <polygon points="695,235 695,380 395,380" fill="#1d1e21"/>
      <polygon points="347,360 230,260 465,260" fill="#1d1e21" opacity="0"/>
      <rect x="240" y="270" width="215" height="80" fill="#1d1e21"/>
    </svg>
    <div class="brand">
      <span class="brand-mark"></span>
      <span class="brand-name">KIVO</span>
    </div>
  </header>

  <h1 class="headline">
    <span class="l1">Specialise in the re-manufacture</span><br>
    <span class="l2">of brakes, hoses and cables</span>
  </h1>

  <section class="products">
    <div class="products-tag">OUR PRODUCTS</div>
    <ul class="product-grid">
      <li class="product"><span class="product-icon"><svg width="22" height="22"><circle cx="11" cy="11" r="7" fill="none" stroke="#f6b90d" stroke-width="3"/></svg></span>Caliper<br>Pistons</li>
      <li class="product"><span class="product-icon"><svg width="22" height="22"><circle cx="11" cy="11" r="7" fill="none" stroke="#f6b90d" stroke-width="3"/></svg></span>Brake Shoes</li>
      <li class="product"><span class="product-icon"><svg width="22" height="22"><circle cx="11" cy="11" r="7" fill="none" stroke="#f6b90d" stroke-width="3"/></svg></span>All Types Of<br>Cables</li>
      <li class="product"><span class="product-icon"><svg width="22" height="22"><circle cx="11" cy="11" r="7" fill="none" stroke="#f6b90d" stroke-width="3"/></svg></span>Seal Kits</li>
      <li class="product"><span class="product-icon"><svg width="22" height="22"><circle cx="11" cy="11" r="7" fill="none" stroke="#f6b90d" stroke-width="3"/></svg></span>Brake Pads</li>
      <li class="product"><span class="product-icon"><svg width="22" height="22"><circle cx="11" cy="11" r="7" fill="none" stroke="#f6b90d" stroke-width="3"/></svg></span>Cables -<br>Accelerator</li>
      <li class="product"><span class="product-icon"><svg width="22" height="22"><circle cx="11" cy="11" r="7" fill="none" stroke="#f6b90d" stroke-width="3"/></svg></span>New Brake<br>Cylinders</li>
      <li class="product"><span class="product-icon"><svg width="22" height="22"><circle cx="11" cy="11" r="7" fill="none" stroke="#f6b90d" stroke-width="3"/></svg></span>Brake Hoses</li>
      <li class="product"><span class="product-icon"><svg width="22" height="22"><circle cx="11" cy="11" r="7" fill="none" stroke="#f6b90d" stroke-width="3"/></svg></span>Clutch Parts</li>
      <li class="product"><span class="product-icon"><svg width="22" height="22"><circle cx="11" cy="11" r="7" fill="none" stroke="#f6b90d" stroke-width="3"/></svg></span>Brake Boosters</li>
      <li class="product"><span class="product-icon"><svg width="22" height="22"><circle cx="11" cy="11" r="7" fill="none" stroke="#f6b90d" stroke-width="3"/></svg></span>Rubber hoses</li>
      <li class="product"><span class="product-icon"><svg width="22" height="22"><circle cx="11" cy="11" r="7" fill="none" stroke="#f6b90d" stroke-width="3"/></svg></span>Hand Brake<br>etc....</li>
    </ul>
  </section>

  <div class="vehicles">Parts For Private, Vintage And Commercial Vehicles</div>

  <section class="parts-strip" role="img" aria-label="Row of product photos: brake shoes, brake pads, calipers, hoses, cables, brake booster and master cylinders">
    <div class="part" style="left:22px;width:120px"></div>
    <div class="part" style="left:156px;width:90px"></div>
    <div class="part" style="left:260px;width:110px"></div>
    <div class="part" style="left:384px;width:80px"></div>
    <div class="part" style="left:478px;width:90px"></div>
    <div class="part" style="left:582px;width:92px"></div>
  </section>

  <div class="aim">Our aim is to repair parts with the quickest turn-around times possible</div>

  <footer class="contact">
    <div class="contact-item"><span class="contact-icon"><svg width="14" height="14" viewBox="0 0 14 14"><rect x="1" y="3" width="12" height="8" fill="none" stroke="#1d1e21" stroke-width="1.5"/><polyline points="1,3 7,8 13,3" fill="none" stroke="#1d1e21" stroke-width="1.5"/></svg></span>parts@kivoautocentre.co.nz</div>
    <div class="contact-item"><span class="contact-icon"><svg width="14" height="14" viewBox="0 0 14 14"><path d="M3 1 L5.5 1 L6.5 4 L5 5.2 Q6.2 8 8.8 9 L10 7.5 L13 8.5 L13 11 Q12.5 13 10.5 13 Q2 12 1 3.5 Q1 1.5 3 1Z" fill="#1d1e21"/></svg></span>0800 555 014 / 07 555 0192</div>
    <div class="contact-item"><span class="contact-icon"><svg width="14" height="14" viewBox="0 0 14 14"><circle cx="7" cy="7" r="5.5" fill="none" stroke="#1d1e21" stroke-width="1.5"/><line x1="1.5" y1="7" x2="12.5" y2="7" stroke="#1d1e21" stroke-width="1.2"/><ellipse cx="7" cy="7" rx="2.4" ry="5.5" fill="none" stroke="#1d1e21" stroke-width="1.2"/></svg></span>www.kivoautocentre.co.nz</div>
  </footer>
</main>
</body>
</html>
```